Need simple and modern looking business card with all my information on one side and logo on the other side
Info :
Company name - VELMAR CONSTRUCTION LLC
Company addres- 418 harbor 87th. Dunmoor park ny 10352
Email- velmarllc@tridomail.Com
Company phone number 555-318-6094
Cell number- 555-742-0583
Web site - velmarllc.Com
My name Gerald tomasino

Target Market(s)

Construction , home improvement, remodeling

Industry/Entity Type

Construction

Contact Information for Business Card

It has to be moder but at the same time simple

Font styles to use
Sans Serif

Colors
0255a3
ffffff
000000
f78f20
b1b1b1
9d9d9d
1b1b1b
33a6d7
ec1f27

Requirements
Must have
• My logo on one side maybe with a some kind of background on the other side all my information
Nice to have
• Some kind of background pictures provided by you .PLEASE HAVE ACCOUNT WITH PIXELVAULT WILL NOT PAY ANY EXTRA FEES .
Should not have
• Any kind of hamer, nails,screws, helmets itp. Please do not copy the other designs come up with something new.

```html
<!DOCTYPE html>
<html lang="en">
<head>
<meta charset="utf-8">
<title>Velmar Construction LLC — Business Card</title>
<link rel="stylesheet" href="https://fonts.googleapis.com/css2?family=Open+Sans:wght@400;600;700&display=swap">
<style>
  :root {
    --page-bg: #e9e4dc;
    --card-bg: #ffffff;
    --brand-blue: #1d76c6;
    --band-grey: #cacaca;
    --accent-red: #ec1f27;
    --accent-orange: #f78f20;
    --ink: #1b1b1b;
    --ink-soft: #333333;
  }
  * { box-sizing: border-box; margin: 0; padding: 0; }
  html, body {
    width: 1200px;
    height: 831px;
    overflow: hidden;
    background: var(--page-bg);
    font-family: "Open Sans", Arial, sans-serif;
    color: var(--ink);
  }
  .business-card {
    position: absolute;
    left: 120px;
    top: 135px;
    width: 960px;
    height: 561px;
    background: var(--card-bg);
    overflow: hidden;
    box-shadow: 0 6px 24px rgba(0,0,0,0.12);
  }
  .card-shapes {
    position: absolute;
    inset: 0;
  }
  .company-mark {
    position: absolute;
    left: 48px;
    top: 150px;
    display: flex;
    align-items: center;
    gap: 18px;
  }
  .company-mark__square {
    width: 34px;
    height: 34px;
    background: var(--accent-orange);
    flex: none;
  }
  .company-mark__name {
    font-size: 33px;
    font-weight: 700;
    line-height: 1.15;
    letter-spacing: 1px;
    color: var(--ink);
  }
  .holder-name {
    position: absolute;
    right: 74px;
    top: 250px;
    font-size: 41px;
    font-weight: 400;
    color: var(--ink);
  }
  .contact-list {
    position: absolute;
    right: 84px;
    top: 355px;
    list-style: none;
  }
  .contact-list li {
    display: flex;
    align-items: center;
    justify-content: flex-end;
    gap: 20px;
    height: 35px;
    font-size: 27px;
    letter-spacing: 1px;
    color: var(--ink-soft);
  }
  .contact-list svg {
    width: 20px;
    height: 20px;
    flex: none;
    fill: var(--ink-soft);
  }
  .address-line {
    position: absolute;
    left: 44px;
    top: 496px;
    display: flex;
    align-items: center;
    gap: 14px;
    font-size: 28px;
    letter-spacing: 1px;
    color: var(--ink-soft);
  }
  .address-line svg {
    width: 20px;
    height: 26px;
    fill: var(--ink-soft);
  }
</style>
</head>
<body>
  <article class="business-card">
    <svg class="card-shapes" width="960" height="561" viewBox="0 0 960 561" aria-hidden="true">
      <polygon class="contact-band" points="333,335 906,335 906,471 240,471" fill="var(--band-grey)"/>
      <rect class="divider-rule" x="0" y="472" width="906" height="6" fill="var(--accent-red)"/>
      <rect class="side-band" x="906" y="0" width="54" height="561" fill="var(--brand-blue)"/>
      <polygon class="side-band__notch" points="906,255 939,280 906,305" fill="var(--card-bg)"/>
    </svg>

    <div class="company-mark">
      <span class="company-mark__square"></span>
      <span class="company-mark__name">VELMAR<br>CONSTRUCTION LLC</span>
    </div>

    <h1 class="holder-name">Gerald tomasino</h1>

    <ul class="contact-list">
      <li>555-318-6094
        <svg viewBox="0 0 24 24"><path d="M6.6 10.8a15.1 15.1 0 0 0 6.6 6.6l2.2-2.2c.3-.3.7-.4 1-.2 1.1.4 2.3.6 3.6.6.6 0 1 .4 1 1V20c0 .6-.4 1-1 1A17 17 0 0 1 3 4c0-.6.4-1 1-1h3.5c.6 0 1 .4 1 1 0 1.3.2 2.5.6 3.6.1.3 0 .7-.2 1z"/></svg>
      </li>
      <li>555-742-0583
        <svg viewBox="0 0 24 24"><path d="M8 1h8a2 2 0 0 1 2 2v18a2 2 0 0 1-2 2H8a2 2 0 0 1-2-2V3a2 2 0 0 1 2-2zm0 3v14h8V4zm4 15.5a1.2 1.2 0 1 0 0 2.4 1.2 1.2 0 0 0 0-2.4z"/></svg>
      </li>
      <li>velmarllc@tridomail.Com
        <svg viewBox="0 0 24 24"><path d="M2 5h20v3l-10 6L2 8zm0 5.3 10 6 10-6V19H2z"/></svg>
      </li>
    </ul>

    <p class="address-line">
      <svg viewBox="0 0 20 26"><path d="M10 0a9 9 0 0 0-9 9c0 6.8 9 17 9 17s9-10.2 9-17a9 9 0 0 0-9-9zm0 12.5A3.5 3.5 0 1 1 10 5.5a3.5 3.5 0 0 1 0 7z"/></svg>
      418 harbor 87th. Dunmoor park ny 10352
    </p>
  </article>
</body>
</html>
```